RAVEL ELECTRICAL GROUP Website Providing Electrical Services

We're a company providing electrical services to the public. We're located in Bankstown a suburb in Sydney, Australia. We are a team of 4 electricians that provide service work to the public. We work on new construction buildings such as single story, double story & units. We also do office fit outs & commercial factory work.

Target Market(s)

All Age Groups
Construction People
Sydney, Australia

Industry/Entity Type

Electrical

Contact Information for Business Card

Name Martin Fells
Contact Number 0412 583 074
Company License 574093B
ABN 54 203 817 465
Residential Commercial Industrial
info@ravelelectrical.example.au

Coding

Coded - Design and coding required

Number of Pages Required

5+ page

Font styles to use
Serif
Sans Serif

Colors

Designer to choose colors to be used in the design.

Requirements
Must have
• WORDPRESS
• Nice & Simple
• Eye catching
• Easy to Read
• Contact details
• Instagram Linked
• Facebook Page Linked
• All Social Media Linked
• Live Chat
• Form Submission
• Testimonial
• Specify services Offered
• About Us (Company details)
• Industrial Installation Page
• Residential Installation Page
• Commercial Installation Page
• Mode of payment (cash, credit-debit card, cheque)
• Local & national electrical news
• Project Videos
• Newsletter
• Level 2 licensed accredited
• Project pictures and articles
• Awards
• Legalities (company's policy, terms, rules)
• FAQ's (Frequently asked questions)
• Collaboration Projects
• Careers
• Projects
• Suppliers
• Customer Perks (discounts or freebies)
• Employees Informations (pictures and basic information)
• Opening Hours and Map location
• Company Logo & Company License (owner license)
• Accreditation
• Customer Service
• Safety/Safety tips
• Clients information (regular clients)
• Expertise
• Company's processes
• Timeline page
• Homepage
• Specify installations
• Search toolbar
• Portfolio
• Request for an appointment - servicing
• Feedbacks
Nice to have
• Articles (better if recent project articles)
• Advertisement
• Influencer Quote
• Sneak Peeks (if you have new services offered)
• Staff Highlights
• Job Hiring (Career Growth)
• Ratings (Rate our service)
• A day/week in the work
• Personal Anecdotes
• Before and after post projects
• Ecological Values
• Marketing feature
• Tagline
• Streaming interactive videos
• Timeline
• Calendar
• Blog
• Emergency Services/Hotline
• Additional services offered
• Transportation (vehicle - car images of our company)
• Comment box (company - clients)
• Rate Us (Performance rating)
Should not have
• Website shouldn't be dark
• Website shouldn't be hard to read
• Advertisement of competitors
• Moving objects
• Dark background

```html
<!DOCTYPE html>
<html lang="en">
<head>
<meta charset="utf-8">
<title>Ravel Electrical Group</title>
<link href="https://fonts.googleapis.com/css2?family=Open+Sans:wght@400;600;700;800&family=Roboto:wght@300;400;500;700&display=swap" rel="stylesheet">
<style>
:root{
  --sky:#5bbde0;
  --navy:#1a5f8c;
  --navy-deep:#15527a;
  --teal:#3cc0a0;
  --azure:#3a9fd6;
  --green:#1e8a4c;
  --yellow:#f5c518;
  --red:#e8554e;
  --orange:#e8841a;
  --ink:#333;
  --muted:#8a8f94;
  --light:#f4f4f4;
  --line:#e2e2e2;
}
*{margin:0;padding:0;box-sizing:border-box}
html,body{width:1200px;height:2699px;overflow:hidden}
body{font-family:"Open Sans",sans-serif;color:var(--ink);background:#fff;position:relative}
section,header,footer,div,a,span,p,h1,h2,h3,li{position:relative}
.abs{position:absolute}
a{text-decoration:none;color:inherit}
ul{list-style:none}

/* top bar */
.topbar{height:36px;background:var(--sky);display:flex;justify-content:flex-end;align-items:center;padding-right:198px;gap:28px;font-size:11px;color:#fff}
.topbar .cta{background:var(--yellow);color:#fff;font-weight:700;font-size:10px;padding:6px 16px;border-radius:2px;text-transform:uppercase}

/* nav */
.nav{height:63px;display:flex;align-items:center;padding:0 198px}
.brand{display:flex;align-items:center;gap:10px;font-family:"Roboto",sans-serif;font-weight:500;font-size:15px;color:var(--navy);letter-spacing:.5px}
.brand .dot{width:22px;height:22px;border-radius:50%;background:var(--navy)}
.menu{margin-left:auto;display:flex;gap:28px;font-size:12px;color:#555;align-items:center}
.menu .call{color:var(--orange);font-weight:700}

/* hero */
.hero{height:459px;background:linear-gradient(110deg,#c9c4bc 0%,#8c8a86 35%,#4b5a78 65%,#2a3556 100%)}
.hero-card{position:absolute;left:171px;top:117px;width:451px;height:219px;background:#fff;padding:30px 32px}
.hero-card .kicker{font-size:15px;color:#333}
.hero-card h1{font-size:27px;font-weight:700;color:var(--navy);line-height:1.13;margin-top:10px}
.hero-card .btn{display:inline-block;margin-top:28px;background:var(--navy);color:#fff;font-size:14px;padding:14px 18px;border-radius:2px}
.arrow{position:absolute;top:214px}

/* quick band */
.quick{height:165px;background:var(--navy)}
.field{position:absolute;left:201px;width:270px;height:31px;background:#fff;font-size:10px;color:#aaa;padding:9px 14px}
.qbtn{position:absolute;top:108px;height:30px;font-size:11px;font-weight:600;display:flex;align-items:center;justify-content:center}
.divider{position:absolute;left:527px;top:28px;width:1px;height:110px;background:rgba(255,255,255,.2)}
.tile{position:absolute;top:27px;width:207px;height:111px;display:flex;align-items:center;gap:14px;padding-left:34px;color:#fff;font-size:13px;line-height:1.25}

/* services */
.services{height:564px;text-align:center}
.services h2{position:absolute;top:76px;width:100%;font-family:"Roboto",sans-serif;font-weight:700;font-size:25px;color:var(--green)}
.services .lead{position:absolute;top:119px;left:300px;width:600px;font-size:12px;line-height:1.3;color:#666}
.card{position:absolute;top:200px;width:270px;height:304px;background:#fff;box-shadow:0 2px 10px rgba(0,0,0,.14);text-align:left;border-top:6px solid}
.card .head{height:88px;background:#f6f6f6;padding:20px 0 0 80px}
.card .head svg{position:absolute;left:26px;top:26px}
.card h3{font-family:"Roboto",sans-serif;font-weight:400;font-size:21px;color:#333}
.card .sub{font-size:10px;color:#aaa;margin-top:4px}
.card ul{position:absolute;left:28px;top:120px;font-size:10px;color:#555}
.card li{height:26px;display:flex;align-items:center;gap:9px}
.card .more{position:absolute;left:28px;top:246px;font-size:10px;color:var(--azure)}
.card .photo{position:absolute;right:0;top:94px;width:132px;height:204px;border-radius:2px}

/* video band */
.video{height:360px;background:var(--navy)}
.video .media{position:absolute;left:0;top:0;width:596px;height:360px;background:linear-gradient(135deg,#4d7aa0,#2d5f88 60%,#3a6f97)}
.play{position:absolute;left:282px;top:155px}
.video .copy{position:absolute;left:713px;top:98px;color:#fff}
.video h2{font-size:19px;font-weight:800;line-height:1.15;letter-spacing:.3px}
.video .small{font-size:12px;margin-top:6px}
.video .phone{font-size:30px;font-weight:700;margin-top:20px;letter-spacing:.5px}
.video .btn{display:inline-block;margin-top:18px;background:var(--sky);font-size:11px;font-weight:700;padding:7px 14px}

/* facts */
.facts{height:428px}
.facts .panel{position:absolute;left:9px;top:9px;width:1182px;height:401px;background:var(--light)}
.facts .label{position:absolute;left:175px;top:90px;font-size:9px;color:#aaa;letter-spacing:.5px}
.facts h2{position:absolute;left:175px;top:106px;font-family:"Roboto",sans-serif;font-weight:500;font-size:27px;color:#222}
.facts .body{position:absolute;left:175px;top:184px;width:370px;font-size:11px;line-height:1.75;color:#9a9a9a}
.facts .body p+p{margin-top:10px}
.stat{position:absolute;width:196px;height:108px;background:#fff;border-left:3px solid;padding:16px 0 0 54px}
.stat svg{position:absolute;left:14px;top:20px}
.stat .num{font-family:"Roboto",sans-serif;font-size:28px;color:#222}
.stat .cap{font-size:9px;color:#bbb;text-transform:uppercase;margin-top:6px;line-height:1.35}

/* reviews */
.reviews{height:287px;background:linear-gradient(90deg,#3b4047,#2b3036 50%,#4a4f55);color:#fff;text-align:center}
.reviews h2{position:absolute;top:54px;width:100%;font-size:23px;font-weight:700}
.reviews .quote{position:absolute;left:255px;top:108px;width:690px;font-size:15px;line-height:1.2}
.reviews .tilde{position:absolute;top:188px;width:100%;font-size:15px}
.reviews .name{position:absolute;top:215px;width:100%;font-size:15px}

/* footer */
.footer{height:258px}
.footer h4{position:absolute;top:44px;font-family:"Roboto",sans-serif;font-weight:400;font-size:14px;color:var(--navy);letter-spacing:.4px}
.footer .col{position:absolute;top:84px;font-size:10px;line-height:19px;color:#555}
.footer .addr{font-weight:400}
.footer .addr b{font-weight:700}
.footer .tel{color:var(--navy);font-weight:700}

.bottom{height:79px;background:var(--navy);color:#fff}
.bottom .copy{position:absolute;left:198px;top:31px;font-size:11px}
.social{position:absolute;left:817px;top:27px;display:flex;gap:16px}
.social span{width:24px;height:24px;border-radius:50%;border:1.5px solid #fff}
</style>
</head>
<body>

<div class="topbar">
  <a>About</a><a>Affiliates</a><a>Blog</a><a>My Account</a>
  <a class="cta">Schedule a Service</a>
</div>

<header class="nav">
  <div class="brand"><span class="dot"></span>RAVEL ELECTRICAL GROUP</div>
  <nav class="menu">
    <a>Home</a><a>Services</a><a>Reviews</a><a>News</a><a>Blog</a><a>Elements</a>
    <a class="call">Call 000 000 0000</a>
    <svg width="16" height="16" viewBox="0 0 16 16"><circle cx="6.5" cy="6.5" r="5" fill="none" stroke="#3a9fd6" stroke-width="1.8"/><line x1="10.2" y1="10.2" x2="14.5" y2="14.5" stroke="#3a9fd6" stroke-width="1.8"/></svg>
  </nav>
</header>

<section class="hero" role="img" aria-label="Photo of an electrician in a yellow hard hat working on a switchboard">
  <div class="hero-card">
    <p class="kicker">Welcome to Ravel Electrical Group</p>
    <h1>We’re your appliance and home improvement experts.</h1>
    <a class="btn">Schedule a Service Now!</a>
  </div>
  <svg class="arrow" style="left:84px" width="20" height="30" viewBox="0 0 20 30"><polyline points="15,2 4,15 15,28" fill="none" stroke="#7fc8ea" stroke-width="2"/></svg>
  <svg class="arrow" style="left:1092px" width="20" height="30" viewBox="0 0 20 30"><polyline points="5,2 16,15 5,28" fill="none" stroke="#7fc8ea" stroke-width="2"/></svg>
</section>

<section class="quick">
  <div class="field" style="top:28px">Enter Your Name</div>
  <div class="field" style="top:68px">Mobile Number</div>
  <a class="qbtn" style="left:201px;width:134px;background:var(--azure);color:#fff">Get Started</a>
  <a class="qbtn" style="left:345px;width:126px;background:#fff;color:var(--navy)">Learn More</a>
  <div class="divider"></div>
  <a class="tile" style="left:572px;background:var(--teal)">
    <svg width="32" height="32" viewBox="0 0 32 32" fill="none" stroke="#fff" stroke-width="1.8"><rect x="3" y="3" width="10" height="10"/><rect x="19" y="3" width="10" height="10"/><rect x="3" y="19" width="10" height="10"/><circle cx="23" cy="23" r="5"/><line x1="27" y1="27" x2="30" y2="30"/></svg>
    <span>See All<br>Our Services</span>
  </a>
  <a class="tile" style="left:793px;background:var(--azure)">
    <svg width="32" height="32" viewBox="0 0 32 32" fill="none" stroke="#fff" stroke-width="1.8"><circle cx="13" cy="12" r="6"/><path d="M3 30c0-6 4-10 10-10s10 4 10 10"/><rect x="20" y="2" width="10" height="7" rx="1"/></svg>
    <span>Free Startup<br>Consultation</span>
  </a>
</section>

<section class="services">
  <h2>Our Services</h2>
  <p class="lead">Our services include formation of business entities, maintenance, compliance as well as working with our diverse clientele to obtain a wide range of regulatory permits, approvals and licenses. We also provide representative office and concierge services.</p>

  <article class="card" style="left:167px;border-color:var(--teal)">
    <div class="head">
      <svg width="38" height="38" viewBox="0 0 38 38" fill="none" stroke="#3cc0a0" stroke-width="1.8"><path d="M5 33L22 16"/><path d="M22 16a7 7 0 1 0 9-9l-4 4-3-1-1-3 4-4a7 7 0 0 0-9 9"/><path d="M5 5l12 12M3 3l4 0 0 4"/><path d="M20 24l9 9 4-4-9-9"/></svg>
      <h3>repair</h3><p class="sub">See all appliances we repair</p>
    </div>
    <ul>
      <li><svg width="10" height="10"><circle cx="5" cy="5" r="5" fill="#3cc0a0"/><polyline points="2.5,5 4.5,7 7.5,3" fill="none" stroke="#fff" stroke-width="1.3"/></svg>Refrigerator</li>
      <li><svg width="10" height="10"><circle cx="5" cy="5" r="5" fill="#3cc0a0"/><polyline points="2.5,5 4.5,7 7.5,3" fill="none" stroke="#fff" stroke-width="1.3"/></svg>Washer</li>
      <li><svg width="10" height="10"><circle cx="5" cy="5" r="5" fill="#3cc0a0"/><polyline points="2.5,5 4.5,7 7.5,3" fill="none" stroke="#fff" stroke-width="1.3"/></svg>Dryer</li>
      <li><svg width="10" height="10"><circle cx="5" cy="5" r="5" fill="#3cc0a0"/><polyline points="2.5,5 4.5,7 7.5,3" fill="none" stroke="#fff" stroke-width="1.3"/></svg>Dishwasher</li>
    </ul>
    <a class="more">View more →</a>
    <div class="photo" role="img" aria-label="Technician in a green work shirt holding a drill" style="background:linear-gradient(180deg,#f2f2f2,#2f8a6a 55%,#24574a)"></div>
  </article>

  <article class="card" style="left:459px;border-color:var(--navy)">
    <div class="head">
      <svg width="38" height="38" viewBox="0 0 38 38" fill="none" stroke="#3cc0a0" stroke-width="1.8"><path d="M4 28L26 6l6 6-22 22H4z"/><line x1="22" y1="10" x2="28" y2="16"/><path d="M6 6l8 8M20 24l8 8"/></svg>
      <h3>improve</h3><p class="sub">Upgrade your home</p>
    </div>
    <ul>
      <li><svg width="10" height="10"><circle cx="5" cy="5" r="5" fill="#3cc0a0"/><polyline points="2.5,5 4.5,7 7.5,3" fill="none" stroke="#fff" stroke-width="1.3"/></svg>Heating &amp; Cooking</li>
      <li><svg width="10" height="10"><circle cx="5" cy="5" r="5" fill="#3cc0a0"/><polyline points="2.5,5 4.5,7 7.5,3" fill="none" stroke="#fff" stroke-width="1.3"/></svg>Window Replacement</li>
      <li><svg width="10" height="10"><circle cx="5" cy="5" r="5" fill="#3cc0a0"/><polyline points="2.5,5 4.5,7 7.5,3" fill="none" stroke="#fff" stroke-width="1.3"/></svg>Kitchen</li>
      <li><svg width="10" height="10"><circle cx="5" cy="5" r="5" fill="#3cc0a0"/><polyline points="2.5,5 4.5,7 7.5,3" fill="none" stroke="#fff" stroke-width="1.3"/></svg>Roofing</li>
    </ul>
    <a class="more">View more →</a>
    <div class="photo" role="img" aria-label="Electrician in blue overalls carrying a coil of cable" style="background:linear-gradient(180deg,#f2f2f2,#3f7fc4 55%,#2a5a92)"></div>
  </article>

  <article class="card" style="left:752px;border-color:var(--yellow)">
    <div class="head">
      <svg width="38" height="38" viewBox="0 0 38 38" fill="none" stroke="#3cc0a0" stroke-width="1.8"><circle cx="19" cy="9" r="4"/><path d="M19 13v8M8 34l11-13 11 13M12 27h14"/></svg>
      <h3>maintain</h3><p class="sub">Learn about home maintenance</p>
    </div>
    <ul>
      <li><svg width="10" height="10"><circle cx="5" cy="5" r="5" fill="#3cc0a0"/><polyline points="2.5,5 4.5,7 7.5,3" fill="none" stroke="#fff" stroke-width="1.3"/></svg>Appliances</li>
      <li><svg width="10" height="10"><circle cx="5" cy="5" r="5" fill="#3cc0a0"/><polyline points="2.5,5 4.5,7 7.5,3" fill="none" stroke="#fff" stroke-width="1.3"/></svg>Heating &amp; Cooling</li>
      <li><svg width="10" height="10"><circle cx="5" cy="5" r="5" fill="#3cc0a0"/><polyline points="2.5,5 4.5,7 7.5,3" fill="none" stroke="#fff" stroke-width="1.3"/></svg>Lawn &amp; Garden</li>
      <li><svg width="10" height="10"><circle cx="5" cy="5" r="5" fill="#3cc0a0"/><polyline points="2.5,5 4.5,7 7.5,3" fill="none" stroke="#fff" stroke-width="1.3"/></svg>Cleaning</li>
    </ul>
    <a class="more">View more →</a>
    <div class="photo" role="img" aria-label="Worker in a yellow hard hat wearing a tool belt" style="background:linear-gradient(180deg,#f2f2f2,#d9a85a 55%,#8a6a3c)"></div>
  </article>
</section>

<section class="video">
  <div class="media" role="img" aria-label="Video still of engineers in hard hats inspecting a warehouse">
    <svg class="play" width="60" height="50" viewBox="0 0 60 50"><rect x="2" y="2" width="56" height="46" rx="9" fill="none" stroke="#fff" stroke-width="3"/><polygon points="23,14 40,25 23,36" fill="#fff"/></svg>
  </div>
  <div class="copy">
    <h2>WE’RE YOUR APPLIANCE AND<br>HOME IMPROVEMENT EXPERTS</h2>
    <p class="small">BOOK ONLINE OR CALL</p>
    <p class="phone">0000 - 000 000 78</p>
    <a class="btn">Book Online Now</a>
  </div>
</section>

<section class="facts">
  <div class="panel"></div>
  <p class="label">STATISTICS</p>
  <h2>some facts</h2>
  <div class="body">
    <p>Our licensed electricians handle every job with care, from new builds and unit blocks to office fit outs and factory work. We keep sites safe, tidy and on schedule for every client.</p>
    <p>Each project is checked against current standards and signed off by a qualified lead, so you can trust the result.</p>
  </div>

  <div class="stat" style="left:615px;top:85px;border-color:var(--teal)">
    <svg width="24" height="18" viewBox="0 0 24 18" fill="#3cc0a0"><circle cx="7" cy="5" r="4"/><circle cx="17" cy="5" r="4"/><path d="M0 18c0-5 3-7 7-7s7 2 7 7zM12 18c0-3 1-5 2-6 1-1 2-1 3-1 4 0 7 2 7 7z"/></svg>
    <p class="num">6,000+</p><p class="cap">Service technicians<br>in the field</p>
  </div>
  <div class="stat" style="left:833px;top:85px;border-color:var(--navy)">
    <svg width="20" height="20" viewBox="0 0 20 20" fill="#3a9fd6"><rect x="1" y="3" width="18" height="16" rx="1"/><rect x="3" y="8" width="14" height="9" fill="#fff"/><rect x="5" y="0" width="2" height="5"/><rect x="13" y="0" width="2" height="5"/></svg>
    <p class="num">10</p><p class="cap">Years average<br>experience</p>
  </div>
  <div class="stat" style="left:615px;top:216px;border-color:var(--yellow)">
    <svg width="20" height="20" viewBox="0 0 20 20"><path d="M2 18l9-9" stroke="#f5c518" stroke-width="3"/><circle cx="14" cy="6" r="5" fill="#f5c518"/><circle cx="16" cy="4" r="2" fill="#fff"/></svg>
    <p class="num">7,500+</p><p class="cap">Repairs last 12<br>months</p>
  </div>
  <div class="stat" style="left:833px;top:216px;border-color:var(--red)">
    <svg width="20" height="20" viewBox="0 0 20 20" fill="#e8554e"><rect x="1" y="9" width="4" height="10"/><path d="M7 9l4-8c2 0 3 1 2 4l-1 3h6c1 0 2 1 1 3l-2 7c0 1-1 1-2 1H7z"/></svg>
    <p class="num">9,000+</p><p class="cap">Happy customers</p>
  </div>
</section>

<section class="reviews" role="img" aria-label="Background photo of a technician working on network cabling, darkened">
  <h2>Customer Reviews</h2>
  <p class="quote">Sed ut perspiciatis unde omnis iste natus error sit voluptatem accusantium doloremque laudantium, totam rem aperiam, eaque ipsa quae ab illo inventore veritatis et quasi architecto beatae vitae dicta sunt explicabo. Nemo enim ipsam voluptatem quia voluptas sit aspernatur aut odit aut fugit, sed quia consequuntur</p>
  <p class="tilde">~~~~~~</p>
  <p class="name">Dana Whitfield</p>
</section>

<footer class="footer">
  <h4 style="left:198px">SERVICE LOCATIONS</h4>
  <h4 style="left:473px">MAINTAIN A BUSINESS</h4>
  <h4 style="left:790px">QUICK LINKS</h4>
  <div class="col addr" style="left:198px;width:240px">
    Suite 4, Chapel House<br><b>12 Kitchener Parade, Bankstown<br>NSW, Sydney.</b><br><br>
    <b>Telephone:</b><br><span class="tel">000 0000 0000</span>
  </div>
  <ul class="col" style="left:473px">
    <li>Our Company</li><li>Certifications</li><li>Our Services</li><li>Company History</li><li>Careers</li><li>Values</li><li>Press Releases</li>
  </ul>
  <ul class="col" style="left:614px">
    <li>Tax Exemption</li><li>Minute Writer</li><li>Data Manager</li><li>Corporate Resolutions</li><li>Site Map</li><li>Become an Affiliate</li>
  </ul>
  <ul class="col" style="left:790px">
    <li>Contact</li><li>About Us</li><li>FAQ</li><li>Affiliate Program</li><li>Legal</li><li>Privacy</li>
  </ul>
  <ul class="col" style="left:913px">
    <li>Support</li><li>Press</li><li>Partners</li><li>Free Consultation</li>
  </ul>
</footer>

<div class="bottom">
  <p class="copy">Copyright 2017 All Rights Reserved</p>
  <div class="social" aria-label="Social media links"><span></span><span></span><span></span><span></span><span></span></div>
</div>

</body>
</html>
```